Welcome Package Cover

We want to design a new cover for our welcome package. The dimensions are 4 1/4" x 9". We are a church in London Ontario called HARBOR Church. Our website is www.harborvellmont.ca
We don't want it to be churchy or religious looking. We want it to be fresh and youthful.
Can use backgrounds unique to London Ontario Canada
I will attach our logo designs.
Religious

```html
<!DOCTYPE html>
<html lang="en">
<head>
<meta charset="utf-8">
<title>HARBOR Church – Welcome Package Cover</title>
<link rel="stylesheet" href="https://fonts.googleapis.com/css2?family=Merriweather:wght@400&family=Open+Sans:wght@400;800&display=swap">
<style>
  :root {
    --sky: #0a9fd8;
    --sky-light: #27b3e6;
    --gold: #e8b24a;
    --tan: #d8c3a0;
    --white: #ffffff;
    --ink: #1b1b1b;
    --brand-navy: #1c2f6b;
  }
  html, body {
    margin: 0;
    padding: 0;
    overflow: hidden;
    background: var(--white);
  }
  .cover {
    position: relative;
    width: 1200px;
    height: 2540px;
    overflow: hidden;
    background: linear-gradient(180deg, var(--sky-light) 0%, var(--sky) 12%, var(--sky) 100%);
  }
  .artwork {
    position: absolute;
    inset: 0;
    width: 1200px;
    height: 2540px;
  }
  .tagline {
    position: absolute;
    left: 78px;
    top: 812px;
    margin: 0;
    font-family: "Merriweather", Georgia, serif;
    font-weight: 400;
    font-size: 61px;
    line-height: 1.3;
    color: var(--white);
    white-space: nowrap;
  }
  .tagline .mark {
    font-size: 84px;
    color: var(--tan);
    line-height: 0;
  }
  .tagline .mark-open {
    position: absolute;
    left: -40px;
    top: 30px;
  }
  .tagline .mark-close {
    margin-left: 10px;
  }
  .footer {
    position: absolute;
    left: 0;
    right: 0;
    bottom: 0;
    height: 240px;
  }
  .contact {
    position: absolute;
    left: 78px;
    top: 66px;
    font-family: "Open Sans", Arial, sans-serif;
    font-size: 42px;
    line-height: 63px;
    color: var(--ink);
  }
  .contact p { margin: 0; }
  .brand {
    position: absolute;
    right: 58px;
    top: 96px;
    display: flex;
    align-items: center;
    gap: 14px;
  }
  .brand-name {
    font-family: "Open Sans", Arial, sans-serif;
    font-weight: 800;
    font-size: 44px;
    line-height: 1;
    color: var(--brand-navy);
  }
  .brand-dot {
    width: 44px;
    height: 44px;
    border-radius: 50%;
    background: var(--gold);
  }
</style>
</head>
<body>
<main class="cover">
  <svg class="artwork" viewBox="0 0 1200 2540" xmlns="http://www.w3.org/2000/svg">
    <defs>
      <radialGradient id="panel-tone" cx="0.35" cy="0.45" r="0.7">
        <stop offset="0" stop-color="#2f6592"/>
        <stop offset="0.6" stop-color="#1f4a73"/>
        <stop offset="1" stop-color="#143555"/>
      </radialGradient>
      <linearGradient id="kids-tone" x1="0" y1="0" x2="1" y2="1">
        <stop offset="0" stop-color="#f3d7c4"/>
        <stop offset="0.5" stop-color="#d99a74"/>
        <stop offset="1" stop-color="#b4452f"/>
      </linearGradient>
      <linearGradient id="family-tone" x1="0" y1="0" x2="1" y2="1">
        <stop offset="0" stop-color="#f1ece6"/>
        <stop offset="0.5" stop-color="#e3c3a5"/>
        <stop offset="1" stop-color="#6c89a8"/>
      </linearGradient>
      <linearGradient id="friends-tone" x1="0" y1="0" x2="0" y2="1">
        <stop offset="0" stop-color="#3f8fdc"/>
        <stop offset="0.45" stop-color="#7ab3e8"/>
        <stop offset="0.75" stop-color="#d9a4a0"/>
        <stop offset="1" stop-color="#3c5a86"/>
      </linearGradient>
      <clipPath id="canvas-clip"><rect width="1200" height="2540"/></clipPath>
    </defs>

    <g clip-path="url(#canvas-clip)">
      <circle cx="30" cy="1010" r="862" fill="none" stroke="var(--gold)" stroke-width="14"
              stroke-dasharray="780 6000" transform="rotate(-95 30 1010)"/>
      <circle cx="30" cy="1010" r="866" fill="none" stroke="var(--tan)" stroke-width="26"
              stroke-dasharray="1290 6000" transform="rotate(-35 30 1010)"/>
      <circle class="feature-panel" cx="30" cy="1010" r="840" fill="url(#panel-tone)"
              role="img" aria-label="Dark blue weathered texture background"/>
    </g>

    <g class="photo photo-kids">
      <circle cx="914" cy="575" r="247" fill="var(--white)"/>
      <circle cx="914" cy="575" r="237" fill="url(#kids-tone)"
              role="img" aria-label="Photo of smiling children in a huddle looking down at the camera"/>
    </g>
    <g class="photo photo-family">
      <circle cx="910" cy="1221" r="256" fill="var(--white)"/>
      <circle cx="910" cy="1221" r="246" fill="url(#family-tone)"
              role="img" aria-label="Photo of a happy young family with two children"/>
    </g>
    <g class="photo photo-friends">
      <circle cx="372" cy="1665" r="327" fill="var(--white)"/>
      <circle cx="372" cy="1665" r="317" fill="url(#friends-tone)"
              role="img" aria-label="Photo of cheering young friends with arms raised under a blue sky"/>
    </g>

    <path d="M0 2300 Q600 2270 1200 2300 L1200 2540 L0 2540 Z" fill="var(--white)"/>
  </svg>

  <p class="tagline"><span class="mark mark-open">“</span>Renewing Lives to<br>Shape Their Worlds.<span class="mark mark-close">„</span></p>

  <footer class="footer">
    <div class="contact">
      <p class="phone">555-014-2290</p>
      <p class="web">www.harborvellmont.ca</p>
    </div>
    <div class="brand">
      <span class="brand-name">HARBOR Church</span>
      <span class="brand-dot"></span>
    </div>
  </footer>
</main>
</body>
</html>
```